Product Label Design

Need a product design for our Epsom salt product, needs to have a luxurious simple feel to it. The picture attached is our brand and wordage on it, the bag we think should be a stand up bag that should be offwhite/creme color. The other picture are products that we like. We updated the packaging to be a Kraft tube box, please see the attached photo for dimensions.

```html
<!DOCTYPE html>
<html lang="en">
<head>
<meta charset="utf-8">
<title>Velmo Awaken – Epsom Salt Pouch</title>
<link rel="stylesheet" href="https://fonts.googleapis.com/css2?family=Open+Sans:wght@400;700&display=swap">
<style>
  :root {
    --backdrop: #e4e3e7;
    --pouch: #eef0ec;
    --pouch-seal: #e6e8e3;
    --ink: #2d2d2b;
    --accent: #72c6e3;
  }
  * { margin: 0; padding: 0; box-sizing: border-box; }
  html, body {
    width: 1200px;
    height: 1000px;
    overflow: hidden;
    background: var(--backdrop);
    font-family: "Open Sans", Arial, sans-serif;
    color: var(--ink);
  }
  .canvas {
    position: relative;
    width: 1200px;
    height: 1000px;
  }
  .pouch {
    position: absolute;
    left: 320px;
    top: 150px;
    width: 560px;
    height: 740px;
    background: var(--pouch);
    overflow: hidden;
  }
  .pouch__seal {
    position: absolute;
    left: 0;
    top: 0;
    width: 100%;
    height: 50px;
    background: var(--pouch-seal);
  }
  .brand-name {
    position: absolute;
    top: 150px;
    width: 100%;
    text-align: center;
    font-weight: 700;
    font-size: 104px;
    line-height: 1;
    letter-spacing: 2px;
    color: var(--ink);
  }
  .variant-name {
    position: absolute;
    top: 322px;
    width: 100%;
    text-align: center;
    font-weight: 700;
    font-size: 34px;
    letter-spacing: 9px;
    color: var(--accent);
  }
  .ingredients {
    position: absolute;
    top: 428px;
    width: 100%;
    text-align: center;
    list-style: none;
    font-size: 18.5px;
    line-height: 30px;
    font-weight: 400;
  }
  .net-weight {
    position: absolute;
    top: 650px;
    width: 100%;
    text-align: center;
    font-size: 15.5px;
    letter-spacing: 2px;
  }
  .pouch__band {
    position: absolute;
    left: 0;
    bottom: 0;
    width: 100%;
    height: 44px;
    background: var(--accent);
  }
</style>
</head>
<body>
  <main class="canvas">
    <section class="pouch" aria-label="Epsom salt stand-up pouch front">
      <div class="pouch__seal"></div>
      <h1 class="brand-name">VELMO</h1>
      <h2 class="variant-name">AWAKEN</h2>
      <ul class="ingredients">
        <li>US Sourced Pure Epsom Salt</li>
        <li>(Magnesium Sulfate)</li>
        <li>+ Abies sibirica</li>
        <li>+ Fir Balsam</li>
      </ul>
      <p class="net-weight">NET WT. 3 LBS (1360 G)</p>
      <div class="pouch__band"></div>
    </section>
  </main>
</body>
</html>
```